Meridel Haulage - Website

A clean, not cluttered informative website for our business. We specialize in the transportation of radioactive materials across North America. The site is mostly for information about our company and will not be used to attract business but will be used to attract employee's mainly drivers. Driver's are very hard to find in our area. One of the pages needs to be a job's posting page with an apply now button. Either an application can be filled out there or a resume can be uploaded which ever functionality works better. I would like a website that I can easily edit, ability to change text and photos.

Number of Pages Required

5+ page

Colors

Designer to choose colors to be used in the design.

Requirements
Must have
• Home - About - Services - Jobs - Contact pages
• A way prospective employee's can apply or upload their resume to be emailed to me
• Very clean apperance
Should not have
• I don't want it to be busy

```html
<!DOCTYPE html>
<html lang="en">
<head>
<meta charset="utf-8">
<title>Meridel Haulage</title>
<link href="https://fonts.googleapis.com/css2?family=Roboto:wght@300;400;500;700&display=swap" rel="stylesheet">
<style>
:root{
  --red:#ef3b42;
  --red-band:#ef4a50;
  --ink:#111111;
  --text:#333333;
  --muted:#6b6b6b;
  --ghost:#e4e4e4;
  --grey-bg:#f1f1f1;
  --white:#ffffff;
  --bar:#a8a8a8;
  --line:#bdbdbd;
}
*{margin:0;padding:0;box-sizing:border-box}
html,body{width:1200px;height:2804px;overflow:hidden}
body{font-family:"Roboto",Arial,sans-serif;color:var(--text);background:var(--white);position:relative}
.abs{position:absolute}

/* header */
.site-header{position:absolute;left:0;top:0;width:1200px;height:77px;background:var(--white);border-bottom:3px solid var(--red)}
.brand{position:absolute;left:163px;top:24px;display:flex;align-items:center;gap:8px;font-weight:700;font-size:19px;color:var(--red);letter-spacing:.5px}
.brand .dot{width:12px;height:12px;border-radius:50%;background:var(--red)}
.main-nav{position:absolute;top:29px;left:0;font-size:11px;color:#555}
.main-nav span{position:absolute;white-space:nowrap}
.flag{position:absolute;left:1013px;top:30px;width:20px;height:12px}

/* hero */
.hero{position:absolute;left:0;top:77px;width:1200px;height:525px;background:linear-gradient(180deg,#cdd3d6 0%,#9da3a6 35%,#6f7475 60%,#4a4d4f 100%)}
.pill{position:absolute;height:27px;width:198px;border-radius:14px;background:var(--red);color:var(--white);font-size:12px;font-weight:500;display:flex;align-items:center;justify-content:center}
.pill svg{position:absolute;left:12px;top:7px;width:14px;height:14px}

/* who we are */
.about{position:absolute;left:0;top:602px;width:1200px;height:292px;background:var(--grey-bg)}
.about-photo{position:absolute;left:0;top:75px;width:385px;height:153px;background:linear-gradient(160deg,#5d7a5c 0%,#8d9a8a 45%,#c9b847 70%,#6f7470 100%)}
.ghost{position:absolute;color:var(--ghost);font-weight:400;white-space:nowrap}
.about h2{position:absolute;left:426px;top:84px;font-size:24px;font-weight:500;color:var(--ink)}
.about p{position:absolute;left:426px;top:124px;width:620px;font-size:12.5px;line-height:15px;color:var(--text)}
.btn{position:absolute;height:29px;border-radius:15px;font-size:12px;display:flex;align-items:center;justify-content:center}
.btn-red{background:var(--red);color:var(--white)}
.btn-white{background:var(--white);color:var(--red)}

/* section heads */
.section-title{position:absolute;left:0;width:1200px;text-align:center;font-size:24px;font-weight:500;color:var(--ink)}
.section-rule{position:absolute;left:286px;width:630px;height:1px;background:var(--line)}
.section-lead{position:absolute;left:320px;width:560px;text-align:center;font-size:12.5px;line-height:18px;color:var(--text)}

/* services */
.service{position:absolute;width:150px;text-align:center}
.service svg{width:38px;height:34px;display:block;margin:0 auto}
.service h3{margin-top:8px;font-size:12.5px;font-weight:500;color:var(--ink)}
.service p{margin-top:14px;font-size:11.5px;line-height:15.5px;color:var(--text);padding:0 12px}

/* jobs band */
.jobs-band{position:absolute;left:0;top:1475px;width:1200px;height:194px;background:linear-gradient(90deg,#f0474d,#ee5a5f 55%,#ef474d)}
.jobs-band h2{position:absolute;left:0;top:42px;width:1200px;text-align:center;font-size:17px;font-weight:500;color:var(--white)}
.jobs-band p{position:absolute;left:310px;top:74px;width:580px;text-align:center;font-size:12.5px;line-height:19px;color:#ffe3e4;height:38px;overflow:hidden}

/* testimonials */
.testimonials{position:absolute;left:0;top:1669px;width:1200px;height:639px;background:var(--grey-bg)}
.quote-card{position:absolute;top:256px;width:206px;height:202px;background:var(--white);box-shadow:0 2px 8px rgba(0,0,0,.08);text-align:center}
.quote-card svg{display:block;margin:26px auto 0;width:20px;height:16px}
.quote-card p{margin:10px 18px 0;font-size:12px;line-height:15px;color:var(--text)}
.quote-card h4{margin-top:14px;font-size:12px;font-weight:500;color:var(--ink)}

/* partners */
.partners{position:absolute;left:0;top:2308px;width:1200px;height:150px;background:var(--white);border-bottom:1px solid #ececec}
.partner{position:absolute;top:60px;width:80px;height:30px;border-radius:4px;background:#d8d8d8}

/* footer */
.site-footer{position:absolute;left:0;top:2458px;width:1200px;height:271px;background:var(--white)}
.footer-brand{position:absolute;left:0;top:52px;width:1200px;display:flex;justify-content:center;align-items:center;gap:8px;font-size:20px;font-weight:700;color:var(--ink)}
.footer-brand .dot{width:12px;height:12px;border-radius:50%;background:var(--ink)}
.footer-text{position:absolute;left:300px;top:116px;width:600px;text-align:center;font-size:11.5px;line-height:18px;color:var(--text)}
.social{position:absolute;top:174px;width:18px;height:18px;border-radius:3px;background:var(--red)}
.copyright{position:absolute;left:0;top:2729px;width:1200px;height:75px;background:var(--bar);color:var(--white);font-size:11px;display:flex;align-items:center;justify-content:center;padding-bottom:10px}
</style>
</head>
<body>

<header class="site-header">
  <div class="brand"><span class="dot"></span>MERIDEL HAULAGE</div>
  <nav class="main-nav">
    <span style="left:664px">Home</span>
    <span style="left:728px">About</span>
    <span style="left:792px">Services</span>
    <span style="left:869px">Jobs</span>
    <span style="left:928px">Contact Us</span>
  </nav>
  <svg class="flag" viewBox="0 0 20 12" role="img" aria-label="English language">
    <rect width="20" height="12" fill="#fff"/>
    <rect y="0" width="20" height="2" fill="#c8202f"/><rect y="4" width="20" height="2" fill="#c8202f"/>
    <rect y="8" width="20" height="2" fill="#c8202f"/>
    <rect width="9" height="6" fill="#2d3f86"/>
  </svg>
</header>

<section class="hero" role="img" aria-label="Photo of a grey semi truck hauling a blue flatbed loaded with large steel containers">
</section>
<div class="pill" style="left:284px;top:542px">
  <svg viewBox="0 0 24 24" fill="none" stroke="#fff" stroke-width="2"><path d="M5 3h4l2 5-3 2a11 11 0 0 0 6 6l2-3 5 2v4a2 2 0 0 1-2 2A17 17 0 0 1 3 5a2 2 0 0 1 2-2z"/></svg>123 456 789</div>
<div class="pill" style="left:501px;top:542px">
  <svg viewBox="0 0 24 24" fill="none" stroke="#fff" stroke-width="2"><rect x="2" y="5" width="20" height="14"/><path d="M2 5l10 8 10-8"/></svg>support@meridelhaulage.com</div>
<div class="pill" style="left:718px;top:542px">
  <svg viewBox="0 0 24 24" fill="none" stroke="#fff" stroke-width="2"><circle cx="12" cy="12" r="9"/><path d="M12 7v5l3 3"/></svg>Lorem Ipsum</div>

<section class="about">
  <div class="about-photo" role="img" aria-label="Photo of a yellow heavy haul truck carrying a large cylindrical load"></div>
  <span class="ghost" style="left:500px;top:76px;font-size:40px">We Are</span>
  <h2>Who We Are</h2>
  <p>Lorem ipsum dolor sit amet, consectetur adipiscing elit, sed do eiusmod tempor incididunt ut labore et dolore magna aliqua. Quis ipsum suspendisse ultrices gravida. Risus commodo viverra maecenas accumsan lacus vel facilisis.</p>
  <div class="btn btn-red" style="left:426px;top:187px;width:133px">Read More</div>
</section>

<section class="services">
  <span class="ghost" style="left:464px;top:958px;font-size:40px">Our Services</span>
  <div class="section-rule" style="top:987px"></div>
  <h2 class="section-title" style="top:972px">Our Services</h2>
  <p class="section-lead" style="top:1020px">Lorem ipsum dolor sit amet, consectetur adipiscing elit, sed do eiusmod tempor incididunt ut labore et dolore magna aliqua. Quis ipsum suspendisse ultrices gravida. Risus commodo viverra maecenas accumsan lacus vel facilisis.</p>

  <div class="service" style="left:185px;top:1145px">
    <svg viewBox="0 0 38 34" fill="none" stroke="#ef3b42" stroke-width="2"><rect x="3" y="9" width="20" height="14"/><path d="M23 13h7l5 5v5H23z"/><circle cx="10" cy="25" r="3"/><circle cx="29" cy="25" r="3"/></svg>
    <h3>Road Freight</h3>
    <p>Lorem ipsum dolor sit amet, consectetur adipiscing elit, sed do eiusmod tempor incididunt ut labore et dolore magna aliqua.</p>
  </div>
  <div class="service" style="left:411px;top:1145px">
    <svg viewBox="0 0 38 34" fill="none" stroke="#ef3b42" stroke-width="2"><path d="M6 28L30 4M30 4l3 3-8 6 2 14-3 2-5-11-6 5v4l-2 2-2-5-5-2 2-2h4l5-6-11-5 2-3 14 2 6-8z"/></svg>
    <h3>Air Freight</h3>
    <p>Lorem ipsum dolor sit amet, consectetur adipiscing elit, sed do eiusmod tempor incididunt ut labore et dolore magna aliqua.</p>
  </div>
  <div class="service" style="left:637px;top:1145px">
    <svg viewBox="0 0 38 34" fill="none" stroke="#ef3b42" stroke-width="2"><rect x="8" y="6" width="22" height="10"/><path d="M15 6v10M23 6v10M3 18h32l-4 9H7z"/></svg>
    <h3>Ocean Freight</h3>
    <p>Lorem ipsum dolor sit amet, consectetur adipiscing elit, sed do eiusmod tempor incididunt ut labore et dolore magna aliqua.</p>
  </div>
  <div class="service" style="left:867px;top:1145px">
    <svg viewBox="0 0 38 34" fill="none" stroke="#ef3b42" stroke-width="2"><path d="M19 3l14 7v14l-14 7-14-7V10z"/><path d="M5 10l14 7 14-7M19 17v14"/></svg>
    <h3>Packaging &amp; Storage</h3>
    <p>Lorem ipsum dolor sit amet, consectetur adipiscing elit, sed do eiusmod tempor incididunt ut labore et dolore magna aliqua.</p>
  </div>

  <div class="btn btn-red" style="left:535px;top:1379px;width:132px">Show All</div>
</section>

<section class="jobs-band">
  <h2>SEARCHING FOR A JOB ?</h2>
  <p>Lorem ipsum dolor sit amet, consectetur adipiscing elit, sed do eiusmod tempor incididunt ut labore et dolore magna aliqua. Quis ipsum suspendisse ultrices gravida. Risus commodo viverra maecenas accumsan lacus vel facilisis.</p>
  <div class="btn btn-white" style="left:534px;top:134px;width:133px">Apply Now</div>
</section>

<section class="testimonials">
  <span class="ghost" style="left:478px;top:80px;font-size:40px">Testimonials</span>
  <div class="section-rule" style="top:103px"></div>
  <h2 class="section-title" style="top:88px">Testimonials</h2>
  <p class="section-lead" style="top:136px">Lorem ipsum dolor sit amet, consectetur adipiscing elit, sed do eiusmod tempor incididunt ut labore et dolore magna aliqua. Quis ipsum suspendisse ultrices gravida. Risus commodo viverra maecenas accumsan lacus vel facilisis.</p>

  <div class="quote-card" style="left:243px">
    <svg viewBox="0 0 20 16" fill="#ef3b42"><rect x="1" y="1" width="7" height="7"/><path d="M5 8h3l-3 7H2z"/><rect x="12" y="1" width="7" height="7"/><path d="M16 8h3l-3 7h-3z"/></svg>
    <p>Lorem ipsum dolor sit amet, consectetur adipiscing elit, sed do eiusmod tempor incididunt ut labore et dolore magna aliqua. Quis ipsum</p>
    <h4>Full Name</h4>
  </div>
  <div class="quote-card" style="left:497px">
    <svg viewBox="0 0 20 16" fill="#ef3b42"><rect x="1" y="1" width="7" height="7"/><path d="M5 8h3l-3 7H2z"/><rect x="12" y="1" width="7" height="7"/><path d="M16 8h3l-3 7h-3z"/></svg>
    <p>Lorem ipsum dolor sit amet, consectetur adipiscing elit, sed do eiusmod tempor incididunt ut labore et dolore magna aliqua. Quis ipsum</p>
    <h4>Full Name</h4>
  </div>
  <div class="quote-card" style="left:753px">
    <svg viewBox="0 0 20 16" fill="#ef3b42"><rect x="1" y="1" width="7" height="7"/><path d="M5 8h3l-3 7H2z"/><rect x="12" y="1" width="7" height="7"/><path d="M16 8h3l-3 7h-3z"/></svg>
    <p>Lorem ipsum dolor sit amet, consectetur adipiscing elit, sed do eiusmod tempor incididunt ut labore et dolore magna aliqua. Quis ipsum</p>
    <h4>Full Name</h4>
  </div>

  <div class="btn btn-red" style="left:534px;top:514px;width:133px">Show All</div>
</section>

<section class="partners" aria-label="Partners">
  <div class="partner" style="left:193px"></div>
  <div class="partner" style="left:388px"></div>
  <div class="partner" style="left:575px"></div>
  <div class="partner" style="left:763px"></div>
  <div class="partner" style="left:945px"></div>
</section>

<footer class="site-footer">
  <div class="footer-brand"><span class="dot"></span>MERIDEL HAULAGE</div>
  <p class="footer-text">Lorem ipsum dolor sit amet, consectetur adipiscing elit, sed do eiusmod tempor incididunt ut labore et dolore magna aliqua. Quis ipsum suspendisse ultrices gravida. Risus commodo viverra maecenas accumsan lacus vel facilisis.</p>
  <div class="social" style="left:542px"></div>
  <div class="social" style="left:566px"></div>
  <div class="social" style="left:591px"></div>
  <div class="social" style="left:615px"></div>
  <div class="social" style="left:640px"></div>
</footer>
<div class="pill" style="left:284px;top:2665px">
  <svg viewBox="0 0 24 24" fill="none" stroke="#fff" stroke-width="2"><path d="M5 3h4l2 5-3 2a11 11 0 0 0 6 6l2-3 5 2v4a2 2 0 0 1-2 2A17 17 0 0 1 3 5a2 2 0 0 1 2-2z"/></svg>123 456 789</div>
<div class="pill" style="left:501px;top:2665px">
  <svg viewBox="0 0 24 24" fill="none" stroke="#fff" stroke-width="2"><rect x="2" y="5" width="20" height="14"/><path d="M2 5l10 8 10-8"/></svg>support@meridelhaulage.com</div>
<div class="pill" style="left:718px;top:2665px">
  <svg viewBox="0 0 24 24" fill="none" stroke="#fff" stroke-width="2"><circle cx="12" cy="12" r="9"/><path d="M12 7v5l3 3"/></svg>Lorem Ipsum</div>

<div class="copyright">Copyright © 2019 Meridel Haulage. All rights reserved.</div>

</body>
</html>
```